DESKWISE Brochure

Would like to revamp an old brochure for a conference
Can I please add our 1300 857 319 in the footer
Printing this on a double sided Brochure

```html
<!DOCTYPE html>
<html lang="en">
<head>
<meta charset="utf-8">
<title>Deskwise – Melbourne's Leading IT Support</title>
<link rel="stylesheet" href="https://fonts.googleapis.com/css2?family=Montserrat:wght@400;500;700;800;900&display=swap">
<style>
  :root {
    --orange: #f27c2c;
    --orange-deep: #e0621a;
    --orange-light: #f7a25e;
    --ink: #1f1d1c;
    --ink-soft: rgba(30, 26, 24, 0.55);
    --white: #ffffff;
  }
  * { margin: 0; padding: 0; box-sizing: border-box; }
  html, body { width: 847px; height: 1200px; overflow: hidden; background: #ddd; }
  body { font-family: "Montserrat", Arial, sans-serif; }

  .brochure {
    position: relative;
    width: 847px;
    height: 1200px;
    overflow: hidden;
    background: linear-gradient(160deg, var(--orange-light) 0%, var(--orange) 35%, var(--orange-deep) 100%);
    color: var(--white);
  }

  /* header */
  .header-band {
    position: absolute; left: 0; top: 0; width: 847px; height: 120px;
  }
  .contact { position: absolute; left: 58px; top: 26px; }
  .contact-phone { font-size: 30px; font-weight: 800; color: var(--orange-deep); letter-spacing: 0.5px; }
  .contact-web { font-size: 15px; font-weight: 600; color: var(--ink); margin-top: 4px; }

  .brand {
    position: absolute; right: 22px; top: 18px;
    display: flex; align-items: center; gap: 12px;
    padding: 14px 20px; background: var(--white);
  }
  .brand-square { width: 30px; height: 30px; background: var(--orange-deep); }
  .brand-name { font-size: 32px; font-weight: 800; color: var(--orange-deep); letter-spacing: 1px; }

  /* title */
  .title-block { position: absolute; left: 100px; top: 168px; width: 640px; }
  .title-line {
    display: block; text-align: center; font-weight: 900; line-height: 1; letter-spacing: -1px;
  }
  .title-line--dark { background: var(--ink); color: var(--white); font-size: 70px; padding: 14px 0 16px; }
  .title-line--light { background: var(--white); color: var(--ink); font-size: 84px; padding: 8px 0 6px; }

  /* intro */
  .intro { position: absolute; left: 170px; top: 462px; width: 560px; }
  .intro-heading { font-size: 23px; font-weight: 800; letter-spacing: 0.3px; }
  .intro-text { font-size: 18px; font-weight: 500; line-height: 1.35; margin-top: 8px; }

  /* services */
  .side-tab {
    position: absolute; left: 0; top: 626px; width: 112px; height: 290px;
    background: var(--ink);
    display: flex; align-items: center; justify-content: center;
  }
  .side-tab-text {
    writing-mode: vertical-rl; transform: rotate(180deg);
    font-size: 19px; font-weight: 800; line-height: 1.15; text-align: center; letter-spacing: 0.5px;
  }
  .services {
    position: absolute; left: 112px; top: 626px; width: 650px; height: 290px;
    background: var(--ink-soft);
    display: grid; grid-template-columns: 1fr 1fr; grid-template-rows: 1fr 1fr;
    padding: 22px 26px; column-gap: 30px; row-gap: 14px;
  }
  .service-title { display: flex; align-items: center; gap: 12px; font-size: 18px; font-weight: 700; }
  .service-icon { width: 28px; height: 28px; flex: none; }
  .service-text { font-size: 12.5px; line-height: 1.4; margin-top: 8px; padding-left: 40px; }

  /* photo */
  .photo {
    position: absolute; left: 0; top: 900px; width: 847px; height: 300px;
    background: linear-gradient(180deg, rgba(224,98,26,0) 0%, #c9a98c 30%, #8d8a86 70%, #5f5e5c 100%);
  }
</style>
</head>
<body>
<main class="brochure">
  <svg class="header-band" viewBox="0 0 847 120" aria-hidden="true">
    <polygon points="0,0 520,0 470,120 0,120" fill="#ffffff"/>
  </svg>

  <div class="contact">
    <div class="contact-phone">1300 857 319</div>
    <div class="contact-web">www.deskwisecomputers.com.au</div>
  </div>

  <div class="brand">
    <span class="brand-square"></span>
    <span class="brand-name">DESKWISE</span>
  </div>

  <h1 class="title-block">
    <span class="title-line title-line--dark">Melbourne's</span>
    <span class="title-line title-line--light">Leading</span>
    <span class="title-line title-line--dark">IT Support</span>
  </h1>

  <section class="intro">
    <h2 class="intro-heading">TAKING CARE OF YOUR IT HEADACHES</h2>
    <p class="intro-text">We partner with all types of businesses to solve their IT problems with continuous ongoing support and solutions that work.</p>
  </section>

  <div class="side-tab"><span class="side-tab-text">CLOUD PHONE<br>SYSTEMS &amp; INTERNET</span></div>

  <section class="services">
    <article class="service">
      <h3 class="service-title">
        <svg class="service-icon" viewBox="0 0 24 24"><rect x="1" y="1" width="22" height="22" rx="3" fill="none" stroke="#fff" stroke-width="1.5"/><path d="M8 6l2 3-1.3 1.3a8 8 0 0 0 5 5L15 14l3 2-1 2.5c-5 0-10-5-10-10z" fill="#fff"/></svg>
        VoIP &amp; Phone Systems
      </h3>
      <p class="service-text">We provide expert services in installation and management for office phone lines, VoIP and communications hardware and systems.</p>
    </article>
    <article class="service">
      <h3 class="service-title">
        <svg class="service-icon" viewBox="0 0 24 24"><path d="M3 4h18v12H9l-5 4v-4H3z" fill="#fff"/></svg>
        SMS Gateway
      </h3>
      <p class="service-text">Unlock seamless communication with our cutting-edge SMS Gateway services, ensuring instant and reliable message delivery for your business needs.</p>
    </article>
    <article class="service">
      <h3 class="service-title">
        <svg class="service-icon" viewBox="0 0 24 24"><circle cx="8" cy="8" r="3.5" fill="#fff"/><circle cx="17" cy="9" r="2.8" fill="#fff"/><path d="M1 20c0-4 3-7 7-7s7 3 7 7z M15 20c0-2.5-.7-4.5-2-6 3.5-1 10 0 10 6z" fill="#fff"/></svg>
        Cloud Teams Calling
      </h3>
      <p class="service-text">Experience the next level of collaboration with our cloud team calling services, empowering your team with seamless communication and features.</p>
    </article>
    <article class="service">
      <h3 class="service-title">
        <svg class="service-icon" viewBox="0 0 24 24"><path d="M2 9a15 15 0 0 1 20 0M5 12.5a10 10 0 0 1 14 0M8.5 16a5 5 0 0 1 7 0" fill="none" stroke="#fff" stroke-width="2" stroke-linecap="round"/><circle cx="12" cy="19.5" r="1.6" fill="#fff"/></svg>
        FTTP, Fibre &amp; 4G Internet
      </h3>
      <p class="service-text">Stay connected, delivering reliable and high-speed connectivity tailored to your business requirements.</p>
    </article>
  </section>

  <div class="photo" role="img" aria-label="Photo of a man working on a laptop at a desk"></div>
</main>
</body>
</html>
```